Bold & Clean Brisk Harbor Stationary Design

Our company, Brisk Harbor Capital Partners needs a business card, letterhead, and envelope design that all also the formatting standards for quickleafpress.com.

Envelope:
Safe Zone: 9.375" x 4"
Trim Size: 9.5" x 4.15"
Bleed Size: 11.125" 8.625"

Letterhead:
Safe Zone: 10.875" x 8.375"
Trim Size: 11" x 8.5"
Bleed Size: 11.125" x 8.625"

Our mailing address is:
2870 W Larkhill St
Chicago, IL 60618

Please make sure the return address on the envelope is formatted correctly for mailing and the logo is not too large.

Please submit designs in word and PDF form.

Our current letterhead is attached.

We would also like a business card with our existing logo that will meet standards for formatting through Quickleaf Press (quickleafpress.com).

These standards are:
Safe Zone: 3.375" x 1.875"
Trim Size: 3.5" x 2"
Bleed Size: 3.625" x 2.125"

The business card is going to be for Marco Lindqvist, President/CEO of Brisk Harbor Capital Partners. Please include the Address, Telephone Number, Cell Phone Number, Fax Number, Email, and Website Address on the card, which are as follows:

2870 W Larkhill St
Chicago, IL 60618

Tel: (773) 555-0172
Cell: (630) 555-0138
Fax: (63) 555-0194
Email: mrl@briskharborcap.com
Web: www.briskharborcap.com

Please make sure that we can easily change the name of the staff member and job position title ourselves as we will be having cards for individual employees in the future as well.

The back of the card should also have the Brisk Harbor logo on it with our services listed:

Financial Planning | Tax | Solutions for Small Businesses

Industry/Entity Type

Accounting

Requirements
Must have
• envelope
• letterhead
• business card
• All meeting standards set out above.

```html
<!DOCTYPE html>
<html lang="en">
<head>
<meta charset="utf-8">
<title>Brisk Harbor Capital Partners – Business Card</title>
<link rel="stylesheet" href="https://fonts.googleapis.com/css2?family=Source+Sans+3:wght@400;600;700&display=swap">
<style>
  :root {
    --navy: #1d2d5e;
    --orange: #f0572a;
    --white: #ffffff;
    --ink-light: #e9edf7;
    --backdrop: #e6e4e0;
    --card-w: 720px;
    --card-h: 411px;
  }
  * { box-sizing: border-box; margin: 0; padding: 0; }
  html, body {
    width: 1200px; height: 1120px; overflow: hidden;
    background: var(--backdrop);
    font-family: "Source Sans 3", "Myriad Pro", Arial, sans-serif;
  }
  .canvas { position: relative; width: 1200px; height: 1120px; }
  .card {
    position: absolute; width: var(--card-w); height: var(--card-h);
    overflow: hidden; box-shadow: 0 6px 18px rgba(0,0,0,.18);
  }

  /* Back of card */
  .card-back { left: 120px; top: 100px; background: var(--navy); color: var(--white); }
  .card-back .brand {
    position: absolute; left: 0; right: 0; top: 112px;
    display: flex; align-items: center; justify-content: center; gap: 16px;
  }
  .brand-dot { width: 26px; height: 26px; border-radius: 50%; background: currentColor; flex: none; }
  .card-back .brand-name { font-size: 38px; font-weight: 600; letter-spacing: .5px; }
  .services {
    position: absolute; left: 0; right: 0; top: 212px;
    display: flex; justify-content: center; gap: 22px;
    list-style: none; font-size: 17px; color: var(--ink-light);
  }
  .services li::before { content: "\2022"; margin-right: 5px; }
  .card-back .website {
    position: absolute; left: 0; right: 0; top: 282px;
    text-align: center; font-size: 21px; letter-spacing: 3.5px; color: var(--ink-light);
  }

  /* Front of card */
  .card-front { left: 360px; top: 610px; background: var(--white); }
  .card-front .shape { position: absolute; inset: 0; }
  .card-front .brand {
    position: absolute; left: 52px; top: 168px; width: 270px;
    display: flex; align-items: center; gap: 12px; color: var(--navy);
  }
  .card-front .brand-dot { width: 22px; height: 22px; }
  .card-front .brand-name { font-size: 26px; font-weight: 600; line-height: 1.1; }
  .contact {
    position: absolute; right: 44px; top: 52px;
    text-align: right; color: var(--white);
  }
  .contact .name { font-size: 21px; font-weight: 700; line-height: 1.1; }
  .contact .title { font-size: 16px; margin-bottom: 26px; }
  .contact .address { font-style: normal; font-size: 16px; line-height: 1.3; margin-bottom: 18px; }
  .contact ul { list-style: none; font-size: 16px; line-height: 1.55; }
  .contact li { display: flex; align-items: center; justify-content: flex-end; gap: 7px; }
  .contact svg { width: 13px; height: 13px; fill: var(--white); flex: none; }
</style>
</head>
<body>
<main class="canvas">

  <section class="card card-back" aria-label="Business card back">
    <div class="brand">
      <span class="brand-dot"></span>
      <span class="brand-name">Brisk Harbor Capital Partners</span>
    </div>
    <ul class="services">
      <li>Financial Planning</li>
      <li>Tax</li>
      <li>Solutions for Small Businesses</li>
    </ul>
    <p class="website">www.briskharborcap.com</p>
  </section>

  <section class="card card-front" aria-label="Business card front">
    <svg class="shape" viewBox="0 0 720 411" preserveAspectRatio="none" aria-hidden="true">
      <circle cx="672" cy="205" r="324" fill="var(--orange)"/>
      <circle cx="684" cy="205" r="324" fill="var(--navy)"/>
    </svg>
    <div class="brand">
      <span class="brand-dot"></span>
      <span class="brand-name">Brisk Harbor<br>Capital Partners</span>
    </div>
    <div class="contact">
      <p class="name">Your Name</p>
      <p class="title">Title</p>
      <address class="address">2870 W Larkhill St<br>Chicago, IL 60618</address>
      <ul>
        <li>
          <svg viewBox="0 0 16 16"><path d="M3.5 1l3 3-1.6 1.8a9 9 0 0 0 5.3 5.3L12 9.5l3 3-2 2.4C6.8 14.3 1.7 9.2 1.1 3z"/></svg>
          (773) 555-0172
        </li>
        <li>
          <svg viewBox="0 0 16 16"><path d="M4.5 0h7a1 1 0 0 1 1 1v14a1 1 0 0 1-1 1h-7a1 1 0 0 1-1-1V1a1 1 0 0 1 1-1zm.8 2v9.5h5.4V2zM8 12.6a1 1 0 1 0 0 2 1 1 0 0 0 0-2z"/></svg>
          (630) 555-0138
        </li>
        <li>
          <svg viewBox="0 0 16 16"><path d="M4 1h8v4H4zM1 6h14v7h-3v2H4v-2H1zm4 4v3.5h6V10z"/></svg>
          (63) 555-0194
        </li>
        <li>
          <svg viewBox="0 0 16 16"><path d="M1 3h14v10H1zm1.5 1.5v.4L8 9l5.5-4.1v-.4z"/></svg>
          mrl@briskharborcap.com
        </li>
        <li>
          <svg viewBox="0 0 16 16"><path d="M8 1a7 7 0 1 0 0 14A7 7 0 0 0 8 1zm0 1.5c.9 1 1.5 2.5 1.6 4.7H6.4C6.5 5 7.1 3.5 8 2.5zM2.6 7.2A5.5 5.5 0 0 1 5.6 3 9 9 0 0 0 5 7.2zm0 1.6H5A9 9 0 0 0 5.6 13a5.5 5.5 0 0 1-3-4.2zm3.8 0h3.2c-.1 2.2-.7 3.7-1.6 4.7-.9-1-1.5-2.5-1.6-4.7zm4.6 0h2.4a5.5 5.5 0 0 1-3 4.2 9 9 0 0 0 .6-4.2zm0-1.6a9 9 0 0 0-.6-4.2 5.5 5.5 0 0 1 3 4.2z"/></svg>
          www.briskharborcap.com
        </li>
      </ul>
    </div>
  </section>

</main>
</body>
</html>
```